High end Coffee Roaster needs a Label design for new Blend

We are looking for a label design for a new blend called "Cold Brew Blend". It is a blend of coffee that we use for making cold brew coffee. The blend is sold as the whole bean and ground coffee in a bag as well as pre-brewed ready to drink in a bottle. We would like the label to be elegant but fun and It must include our logo. Please check out or website brightmilebeans.com or social media @brightmilebeans for information on our company and our coffees if you need more ideas on the kind of product we offer and our style.
Updates

Requirements
Must have
• Our Company Logo. Creative design.
Should not have
• This project should NOT be a corporate company logo, Please do NOT submit a design for a company logo this is a project for a Label. We already have a logo and we are looking for a design on a label. I have uploaded several examples of what we are looking for. Those examples are from other coffee companies who have cold brew. Those are examples only to give you a better idea of what im looking for. DO NOT COPY THEM.

```html
<!DOCTYPE html>
<html lang="en">
<head>
<meta charset="utf-8">
<title>Cold Brew Blend Label</title>
<link href="https://fonts.googleapis.com/css2?family=Oswald:wght@400;500;700&family=Kaushan+Script&display=swap" rel="stylesheet">
<style>
  :root {
    --backdrop: #c8b48c;
    --plum: #3b2431;
    --plum-deep: #2f1b27;
    --frame: #7d6672;
    --gold: #e3a92a;
    --gold-band: #d9a21e;
    --amber: #f0b92b;
    --rust: #d46a2a;
    --cream: #f4eee6;
  }
  * { margin: 0; padding: 0; box-sizing: border-box; }
  html, body { width: 1200px; height: 789px; overflow: hidden; background: var(--backdrop); }
  .canvas { position: relative; width: 1200px; height: 789px; }
  .bag { position: absolute; left: 390px; top: 20px; width: 420px; height: 749px; background: var(--plum); overflow: hidden; }
  .band { position: absolute; left: 0; width: 100%; background: var(--gold-band); }
  .band--top { top: 0; height: 38px; }
  .band--bottom { bottom: 0; height: 40px; }
  .frame-art { position: absolute; left: 0; top: 0; }
  .brand { position: absolute; top: 200px; left: 0; width: 100%; display: flex; justify-content: center; align-items: center; gap: 10px; }
  .brand__dot { width: 16px; height: 16px; border-radius: 50%; background: var(--gold); }
  .brand__name { font-family: "Oswald", sans-serif; font-weight: 500; font-size: 24px; letter-spacing: 2px; color: var(--cream); }
  .title-script { position: absolute; top: 262px; left: 0; width: 100%; text-align: center; font-family: "Kaushan Script", cursive; font-size: 52px; line-height: 1.2; color: var(--gold); transform: rotate(-8deg); }
  .title-main { position: absolute; top: 340px; left: 0; width: 100%; height: 128px; text-align: center; font-family: "Oswald", sans-serif; font-weight: 500; font-size: 112px; line-height: 128px; color: var(--cream); letter-spacing: 4px; }
  .divider { position: absolute; top: 478px; left: 90px; width: 240px; height: 12px; }
  .subtitle { position: absolute; top: 494px; left: 0; width: 100%; text-align: center; font-family: "Oswald", sans-serif; font-weight: 500; font-size: 38px; line-height: 1.2; color: var(--gold); letter-spacing: 1px; }
  .tags { position: absolute; top: 556px; left: 0; width: 100%; display: flex; justify-content: center; gap: 6px; align-items: stretch; }
  .tag { font-family: "Oswald", sans-serif; display: flex; align-items: center; justify-content: center; text-align: center; padding: 3px 6px; }
  .tag--ground { background: var(--rust); color: var(--cream); font-size: 10px; line-height: 1.1; width: 56px; }
  .tag--premium { background: var(--amber); color: var(--plum-deep); font-weight: 700; font-size: 14px; padding: 6px 10px; }
  .tag--size { background: var(--rust); color: var(--cream); flex-direction: column; width: 48px; line-height: 1; }
  .tag--size strong { font-size: 19px; }
  .tag--size span { font-size: 9px; }
  .credit { position: absolute; top: 604px; left: 0; width: 100%; text-align: center; font-family: "Oswald", sans-serif; font-size: 12px; letter-spacing: 0.5px; color: var(--cream); }
  .handle { position: absolute; top: 626px; left: 0; width: 100%; text-align: center; font-family: "Oswald", sans-serif; font-weight: 400; font-size: 12px; color: var(--frame); }
</style>
</head>
<body>
<main class="canvas">
  <section class="bag">
    <div class="band band--top"></div>
    <svg class="frame-art" width="420" height="749" viewBox="0 0 420 749">
      <path d="M80 680 V210 A130 130 0 0 1 340 210 V680 Z" fill="var(--plum-deep)"/>
      <g fill="none" stroke="var(--frame)" stroke-width="1.5">
        <path d="M80 250 H40 V700 H380 V250 H340"/>
        <path d="M80 258 H48 V692 H372 V258 H340"/>
      </g>
    </svg>
    <div class="brand">
      <span class="brand__dot"></span>
      <span class="brand__name">BRIGHT MILE BEANS</span>
    </div>
    <div class="title-script">Cold Brew</div>
    <div class="title-main">BLEND</div>
    <svg class="divider" width="240" height="12" viewBox="0 0 240 12">
      <g fill="none" stroke="var(--gold)" stroke-width="1.2">
        <path d="M0 6 H108 M132 6 H240"/>
        <path d="M112 6 l8 -5 l8 5 l-8 5 Z"/>
      </g>
    </svg>
    <div class="subtitle">ARTISAN ROASTED</div>
    <div class="tags">
      <div class="tag tag--ground">GROUND COFFEE</div>
      <div class="tag tag--premium">PREMIUM COFFEE BLEND</div>
      <div class="tag tag--size"><strong>16</strong><span>ML.OZ</span></div>
    </div>
    <p class="credit">BREWED AND BOTTLED BY BRIGHT MILE BEANS</p>
    <p class="handle">@brightmilebeans</p>
    <div class="band band--bottom"></div>
  </section>
</main>
</body>
</html>
```